Business Card Design for Tarlo Cosmetics

hair extension supplier and mobile technican
make up and make up artistry
cosmetic eye contacts
eye lashes
general facial and hair products

```html
<!DOCTYPE html>
<html lang="en">
<head>
<meta charset="utf-8">
<title>Tarlo Cosmetics — Business Card</title>
<link href="https://fonts.googleapis.com/css2?family=Parisienne&display=swap" rel="stylesheet">
<style>
  :root {
    --page: #ffffff;
    --card: #000000;
    --ink: #ffffff;
    --accent: #e3963c;
    --rule: #bff0f4;
    --art-light: #2a2a2a;
    --ornament-light: #ffffff;
    --ornament-dark: #9a9a9a;
    --script: "Parisienne", cursive;
  }
  * { margin: 0; padding: 0; box-sizing: border-box; }
  html, body {
    width: 1200px;
    height: 707px;
    overflow: hidden;
    background: var(--page);
  }
  .canvas {
    position: relative;
    width: 1200px;
    height: 707px;
    background: var(--page);
  }
  .card {
    position: absolute;
    left: 57px;
    top: 38px;
    width: 1082px;
    height: 607px;
    background: var(--card);
    border-radius: 190px 36px 36px 70px;
    overflow: hidden;
  }
  .profile-art {
    position: absolute;
    left: 0;
    top: 0;
    width: 380px;
    height: 100%;
    background: linear-gradient(90deg, var(--art-light) 0%, var(--card) 100%);
  }
  .ornament-art {
    position: absolute;
    left: 206px;
    top: 365px;
    width: 100px;
    height: 100px;
    border-radius: 50%;
    background: radial-gradient(circle at 50% 40%, var(--ornament-dark) 0%, var(--ornament-light) 70%);
  }
  .brand-name {
    position: absolute;
    right: 40px;
    top: 62px;
    font-family: var(--script);
    font-weight: 400;
    font-size: 70px;
    line-height: 1;
    color: var(--ink);
    white-space: nowrap;
  }
  .line {
    position: absolute;
    right: 28px;
    text-align: right;
    color: var(--ink);
    font-family: var(--script);
    white-space: nowrap;
    line-height: 1;
  }
  .person-name { top: 384px; font-size: 50px; }
  .person-mobile { top: 437px; font-size: 24px; }
  .divider {
    position: absolute;
    left: 543px;
    right: 0;
    top: 481px;
    height: 4px;
    background: var(--accent);
  }
  .contact-address { top: 505px; font-size: 27px; }
  .contact-email { top: 545px; font-size: 26px; }
  .baseline-rule {
    position: absolute;
    left: 0;
    right: 0;
    top: 647px;
    height: 1px;
    background: var(--rule);
  }
</style>
</head>
<body>
  <main class="canvas">
    <section class="card">
      <div class="profile-art" role="img" aria-label="Black silhouette of a woman's head in profile forming the card's left edge"></div>
      <div class="ornament-art" role="img" aria-label="White spiral earring ornament"></div>
      <div class="brand-name">Tarlo Cosmetics</div>
      <p class="line person-name">Mirela Santoro</p>
      <p class="line person-mobile">mobile 0400 123 987</p>
      <div class="divider"></div>
      <p class="line contact-address">18 harlow st, Eastvale, WA, 6099</p>
      <p class="line contact-email">email mirela@tarlocosmetics.com.au</p>
    </section>
    <div class="baseline-rule"></div>
  </main>
</body>
</html>
```